Media Browser and player web application

I need to redesign a web application that enables to browse a media server (Lumarra) contents (images, audio, video) and play it in a web player.

Current implementation of the application can be seen at: http://www.kelbofaq.net/content/demonstration-lumarra-pro-online-media-browser

This refresh is aiming to:
1) make the application simpler, based on typology (think Panelix Tile style, VidHalo, Flickro); a simple fan concept is here: http://tow.gandeliq.net/lumarra/
2) make the application work on desktop as well as touch screen devices (ie no hover functionality, no pagination, large touch controls)
3) fast (remove unnecessary animations)
4) design with the app being responsive in mind

The attached UX designs show the basic flows in the application. Please note that the placement of controls (for example) is not set in stone and I welcome your input on the layout.

Ideally the default theme will be dark. Items' thumbnails will be square place holders, with images fit in them depending on the item icons' aspect ratio.

Also attaching the product's logo (Lumarra) and icon. The web application's name is ClipRoamer (or Lumarra ClipRoamer), so it should be included in the design (the UX designs include place holder Lumarra logo in the left top corner).

The main categories for each file type are (you will have to provide an icon for each of these):
- Audio: Albums, Artists, Album artists, Folders, Genres, Composers, Titles, Random music, Random albums, Last listened, Playlists, Online
- Image: Albums, Folders, Year, Month, Playlists, Online
- Video: Titles, Movies, Series, Folders, Last viewed, Last added, Genres, Actors, Directors, Producers, Release years, Playlists, Online
Updates

Target Market(s)

Mostly tech enthusiasts who want to stream their media over the internet to their devices.

Industry/Entity Type

Artists

Requirements
Must have
• Designs for all the provided UX designs
Touch-friendly web application design
High-res (Retina) assets
Light, type based Tile-like design
Nice to have
• Responsive web version
Dark and Light theme switching.
Should not have
• Chrome
Heavy graphics (eg backgrounds) that take time to load

```html
<!DOCTYPE html>
<html lang="en">
<head>
<meta charset="utf-8">
<title>Lumarra ClipRoamer – Login</title>
<link rel="stylesheet" href="https://fonts.googleapis.com/css2?family=Questrial&display=swap">
<style>
  :root {
    --bg-center: #2a587d;
    --bg-mid: #214e74;
    --bg-edge: #072848;
    --brand-blue: #0a9be0;
    --brand-edge: #22415e;
    --panel: #2d323d;
    --panel-border: #1c2029;
    --field: #383c49;
    --field-text: #c9ccd3;
    --title: #ffffff;
    --button: #129fd9;
    --button-text: #263445;
    --art-light: #e6e9ee;
    --art-mid: #9ea4ad;
    --art-dark: #4a4f58;
  }
  * { box-sizing: border-box; margin: 0; padding: 0; }
  html, body { width: 1200px; height: 1000px; overflow: hidden; }
  body {
    position: relative;
    font-family: "Questrial", sans-serif;
  }
  .backdrop {
    position: absolute; inset: 0;
    background: radial-gradient(ellipse 75% 70% at 50% 48%, var(--bg-center) 0%, var(--bg-mid) 55%, var(--bg-edge) 100%);
  }
  .brand {
    position: absolute; left: 78px; top: 0; width: 272px; height: 150px;
    background: var(--brand-blue);
    border-right: 8px solid var(--brand-edge);
    display: flex; align-items: center; justify-content: center;
  }
  .brand-name { color: #fff; font-size: 50px; letter-spacing: 1px; text-transform: lowercase; }
  .login-card {
    position: absolute; left: 178px; top: 293px; width: 843px; height: 375px;
    display: flex;
  }
  .login-form {
    width: 468px; height: 100%;
    background: var(--panel); border: 1px solid var(--panel-border);
    padding: 77px 0 0 78px;
  }
  .login-title {
    color: var(--title); font-weight: 400; font-size: 20px; letter-spacing: 0.3px;
    line-height: 24px;
    margin-bottom: 22px;
  }
  .field {
    display: block; width: 306px; height: 40px; margin-bottom: 13px;
    background: var(--field); border: none; padding: 0 15px;
    font-family: inherit; font-size: 14px; color: var(--field-text);
  }
  .field::placeholder { color: var(--field-text); }
  .login-button {
    display: flex; align-items: center; gap: 6px;
    margin: 45px 0 0 204px; width: 102px; height: 34px; justify-content: center;
    background: var(--button); border: none; color: var(--button-text);
    font-family: inherit; font-size: 16px;
  }
  .login-art {
    width: 375px; height: 100%;
    background:
      radial-gradient(circle at 105% 50%, var(--art-light) 0%, #c9cdd3 30%, var(--art-mid) 55%, var(--art-dark) 100%);
  }
</style>
</head>
<body>
  <div class="backdrop" role="img" aria-label="Deep blue backdrop with a light blue folded ribbon winding behind the login card"></div>

  <header class="brand">
    <span class="brand-name">Lumarra</span>
  </header>

  <main class="login-card">
    <form class="login-form">
      <h1 class="login-title">LOGIN INTO CLIPROAMER</h1>
      <input class="field" type="text" placeholder="username">
      <input class="field" type="password" placeholder="password">
      <button class="login-button" type="submit">
        <svg width="13" height="14" viewBox="0 0 13 14" aria-hidden="true">
          <path d="M3.5 6V4a3 3 0 0 1 6 0v2" fill="none" stroke="var(--button-text)" stroke-width="1.8"/>
          <rect x="1.5" y="6" width="10" height="8" rx="1" fill="var(--button-text)"/>
        </svg>
        LOGIN
      </button>
    </form>
    <div class="login-art" role="img" aria-label="Abstract grey light rays radiating from the right edge"></div>
  </main>
</body>
</html>
```